KVO-Business Card Design

I need a modern, professional business card design that includes my logo as the main feature, maybe the entire background with the contact info overlaying or even contact info on the back and the logo full frontal

Neat and organized placement of contact information

Would like to see options in black and white

Target Market(s)

real estate Developers, Construction managers, business and home owners

Industry/Entity Type

Construction

Contact Information for Business Card

KVO Construction
Danny Ferrante
General Contractor

Office: 1-888-902-7315 Ext #1
Cell: 215-730-4162
Fax: 1-888-902-7315

Font styles to use
Serif

Requirements
Must have
• title
• office #
• cell #
• Email
• website
Nice to have
• fax

```html
<!DOCTYPE html>
<html lang="en">
<head>
<meta charset="utf-8">
<title>KVO Construction – Business Card</title>
<link rel="stylesheet" href="https://fonts.googleapis.com/css2?family=Open+Sans:wght@400;600;700&display=swap">
<style>
  :root {
    --stage: #141414;
    --paper: #ffffff;
    --green: #4aa832;
    --green-dark: #1f7a36;
    --green-light: #8ddc55;
    --green-deep: #1f8a3e;
    --ink: #333333;
    --white: #ffffff;
  }
  * { margin: 0; padding: 0; box-sizing: border-box; }
  html, body { width: 1200px; height: 900px; overflow: hidden; }
  body {
    background: var(--stage);
    font-family: "Open Sans", Arial, sans-serif;
    position: relative;
  }
  .card {
    position: absolute;
    top: 170px;
    width: 347px;
    height: 561px;
    box-shadow: 0 4px 14px rgba(0,0,0,0.5);
  }
  .card-front { left: 259px; background: var(--paper); }
  .card-back {
    left: 631px;
    background: linear-gradient(to bottom, var(--green-light), var(--green-deep));
  }
  .tab {
    position: absolute;
    left: 102px;
    width: 143px;
    height: 29px;
    background: linear-gradient(to bottom, var(--green-light), var(--green));
  }
  .tab-top { top: 0; }
  .tab-bottom { bottom: 0; }
  .brand {
    position: absolute;
    left: 0;
    width: 100%;
    display: flex;
    align-items: center;
    justify-content: center;
    gap: 10px;
    font-weight: 700;
    font-size: 30px;
    letter-spacing: 1px;
  }
  .brand-mark { width: 18px; height: 18px; display: inline-block; }
  .card-front .brand { top: 170px; color: var(--green-dark); }
  .card-front .brand-mark { background: var(--green); }
  .card-back .brand { top: 280px; color: var(--white); }
  .card-back .brand-mark { background: var(--white); }
  .contact {
    position: absolute;
    top: 309px;
    left: 0;
    width: 100%;
    text-align: center;
    color: var(--ink);
    font-size: 14.5px;
    line-height: 20.5px;
  }
  .contact-name { color: var(--green); font-weight: 600; font-size: 19px; line-height: 24px; }
  .contact-title { margin-bottom: 20px; }
  .contact-label { color: var(--green-dark); font-weight: 700; }
  .contact-phones { margin-bottom: 20px; }
</style>
</head>
<body>
  <section class="card card-front">
    <div class="tab tab-top"></div>
    <div class="brand"><span class="brand-mark"></span>KVO Construction</div>
    <div class="contact">
      <p class="contact-name">Danny Ferrante</p>
      <p class="contact-title">General Contractor</p>
      <div class="contact-phones">
        <p><span class="contact-label">P:</span>1-888-902-7315 Ext #1</p>
        <p><span class="contact-label">M:</span> 215-730-4162</p>
        <p><span class="contact-label">F:</span>1-888-902-7315</p>
      </div>
      <p>info@kvoconstruction.com</p>
      <p>www.kvoconstruction.com</p>
    </div>
    <div class="tab tab-bottom"></div>
  </section>

  <section class="card card-back">
    <div class="brand"><span class="brand-mark"></span>KVO Construction</div>
  </section>
</body>
</html>
```